2 page brouchure for a Property Valuation company.

We require a 2 page brochure (printed front and back) for a property valuation company known as 'Quorvel Valuations'.

Quorvel valuations provides independent, reliable, accurate valuation services to our clients on the value of their properties to enable confidence and certainty in their decision.

The brochure is to be used to convey that the company provides valuation services for 8 main purposes and across 4 different property types.

The 8 main purposes for valuation include:
- Pre-Purchase Valuations
- Stamp Duty Valuations
-Capital Gains Tax (CGT)Valuations
-Unit Entitlement Valuations
-Family Law and Litigation Valuations
-Easement Valuations
-Wills & Probate Valuations
-Insolvency/Asset Realisation Valuations

The 4 main property types are:
-Residential
-Commercial
-Industrial
-Retail.

The brochure should have a title page, a page for the services, a page for the property types and a rear page with contact details.
Contact detail will include;
email:
phone :
Post :
website:

The words 'property valuation and advisory services' should be used at the front of the brochure.

The brochure should be professional and is used to convey information using visual aid and is to be used for promotion.

Our main colors are dark green and grey as seen in our logo.

We have attached our logo to add to the brochure and visit our website at: www.quorvelvaluations-example.com.au for more information about the company.

Please let me know if there are any further questions.

Target Market(s)

Solicitors/Lawyers
Accountants
Surveyors
Builders/Developers

Requirements
Must have
• Logo Colors, Logo, 8 Main services, 4 main property types, contact details.
Nice to have
• Should have concise visual aids to convey message.

Please add that we provide fast 48 hour turnaround for short form valuations. Maybe use a visual aid to convey this.

```html
<!DOCTYPE html>
<html lang="en">
<head>
<meta charset="utf-8">
<title>Quorvel Valuations – Brochure</title>
<link href="https://fonts.googleapis.com/css2?family=Roboto:wght@400;500;700&family=Roboto+Condensed:wght@700&display=swap" rel="stylesheet">
<style>
:root{
  --green:#17703c;
  --green-dark:#0f5e31;
  --green-light:#5ea57a;
  --grey:#5b5b5b;
  --grey-text:#6a6a6a;
  --panel:#d9d9d7;
  --stage:#4a4a4a;
  --white:#ffffff;
}
*{margin:0;padding:0;box-sizing:border-box}
html,body{width:750px;height:1200px;overflow:hidden;background:var(--stage);font-family:"Roboto",Arial,sans-serif;color:var(--grey-text)}
.page{position:absolute;background:var(--white);overflow:hidden;box-shadow:0 3px 10px rgba(0,0,0,.45)}
.abs{position:absolute}
.photo{position:absolute}
.brand{position:absolute;display:flex;align-items:center;gap:7px}
.brand-mark{background:var(--green)}
.brand-name{font-family:"Roboto",Arial,sans-serif;font-weight:500;color:var(--grey);letter-spacing:.18em;text-transform:uppercase;line-height:1.05}
.badge{position:absolute;background:var(--green);border-radius:2px}
/* cover */
.cover{left:257px;top:16px;width:236px;height:336px}
.cover .brand{left:11px;top:14px}
.cover .brand-mark{width:30px;height:30px}
.cover .brand-name{font-size:9.5px}
.cover-block{left:174px;top:64px;width:62px;height:81px;background:var(--green)}
.cover-title{left:9px;top:80px;font-family:"Roboto Condensed",Arial,sans-serif;font-weight:700;font-size:12.6px;line-height:1.27;color:var(--green)}
.cover-sub{left:9px;top:113px;font-size:6.9px;line-height:1.55;color:var(--grey)}
.cover-url{left:5px;top:319px;font-size:6.5px;color:var(--green);font-weight:500}
/* spread */
.spread{left:62px;top:362px;width:625px;height:445px}
.spread .right-page{left:312px;top:76px;width:313px;height:369px;background:var(--panel)}
.spread .brand{left:13px;top:35px}
.spread .brand-mark{width:32px;height:32px}
.spread .brand-name{font-size:10.5px}
.about-title{left:22px;top:219px;font-size:9px;font-weight:700;color:var(--green)}
.about-body{left:22px;top:232px;width:128px;font-size:4.4px;line-height:1.4}
.about-body p{margin-bottom:5.2px}
.purposes-title{left:163px;top:92px;font-size:9px;font-weight:700;line-height:1.1;color:var(--grey)}
.purpose{position:absolute;left:160px;width:146px;display:flex;gap:6px}
.purpose svg{flex:0 0 17px;width:17px;height:17px;fill:var(--green)}
.purpose h3{font-size:6px;font-weight:700;color:var(--green);line-height:1.1}
.purpose p{font-size:4.3px;line-height:1.35;color:var(--green)}
.types-tab{left:344px;top:74px;padding:2px 6px;background:var(--green);color:var(--white);font-size:8.5px;font-weight:700}
.type{position:absolute;width:108px}
.type .photo{position:relative;width:104px;height:73px}
.type h3{font-size:8.8px;font-weight:700;color:var(--green);margin:4px 0 4px 3px}
.type p,.type li{font-size:4.3px;line-height:1.4;margin-left:3px}
.type ul{list-style:none;margin-left:3px}
.type li::before{content:"•";display:inline-block;width:13px}
/* back */
.back{left:246px;top:812px;width:259px;height:367px}
.turnaround{left:153px;top:9px;width:90px;height:90px}
.turn-num{left:176px;top:16px;width:44px;text-align:center;font-size:32px;color:var(--green-dark);line-height:1}
.turn-text{left:163px;top:50px;width:70px;text-align:center;font-size:7.6px;font-weight:700;color:var(--green);line-height:1.1}
.back-green{left:0;top:222px;width:259px;height:120px}
.guarantee-title{left:25px;top:243px;font-size:8.5px;font-weight:500;color:var(--white)}
.guarantee-list{left:33px;top:258px;width:100px;list-style:none;font-size:5px;line-height:1.3;color:var(--white)}
.guarantee-list li{margin-bottom:1.7px;position:relative}
.guarantee-list li::before{content:"•";position:absolute;left:-10px}
.divider{left:130px;top:246px;width:1px;height:75px;background:rgba(255,255,255,.6)}
.contact-title{left:139px;top:245px;font-size:8.4px;font-weight:500;color:var(--white)}
.contact-list{left:139px;top:264px;list-style:none;font-size:6px;color:var(--white)}
.contact-list li{display:flex;align-items:center;gap:5px;height:11.5px}
.contact-list svg{width:8px;height:8px;fill:var(--white)}
.back .brand{left:8px;top:338px}
.back .brand-mark{width:20px;height:20px}
.back .brand-name{font-size:7.8px}
</style>
</head>
<body>

<!-- Cover page -->
<section class="page cover">
  <div class="brand"><span class="brand-mark"></span><span class="brand-name">Quorvel<br>Valuations</span></div>
  <div class="abs cover-block"></div>
  <h1 class="abs cover-title">PROPERTY VALUATION<br>AND ADVISORY SERVICES</h1>
  <p class="abs cover-sub">TO INDIVIDUALS, INVESTORS,<br>DEVELOPERS AND ORGANIZATIONS</p>
  <div class="photo" style="left:0;top:148px;width:114px;height:77px;background:linear-gradient(160deg,#3f6fa8,#1d3457 60%,#5b5a3c)" role="img" aria-label="Glass office tower at dusk"></div>
  <div class="photo" style="left:117px;top:148px;width:119px;height:77px;background:linear-gradient(180deg,#b9cfe6,#d8d6cf 45%,#7e9a55)" role="img" aria-label="Modern apartment block with a garden path"></div>
  <div class="photo" style="left:0;top:227px;width:104px;height:72px;background:linear-gradient(180deg,#e8e2d8,#b99f80 60%,#7a6a5a)" role="img" aria-label="Interior atrium of a shopping centre"></div>
  <div class="photo" style="left:107px;top:227px;width:129px;height:72px;background:linear-gradient(120deg,#2c4f6e,#7fa4c4 45%,#1f3550)" role="img" aria-label="Warehouse interior with a person holding a tablet"></div>
  <p class="abs cover-url">www.quorvelvaluations-example.com.au</p>
  <div class="badge" style="left:176px;top:311px;width:46px;height:19px"></div>
</section>

<!-- Inside spread -->
<section class="page spread">
  <div class="abs right-page"></div>
  <div class="photo" style="left:167px;top:0;width:273px;height:76px;background:linear-gradient(180deg,#9fc3e3,#dfe9f2 55%,#6d7a86)" role="img" aria-label="Hand holding a tablet showing a building"></div>
  <div class="photo" style="left:440px;top:0;width:185px;height:76px;background:linear-gradient(90deg,#eef0ee,#d6dcd8)" role="img" aria-label="Hand drawing on a land subdivision plan"></div>
  <div class="brand"><span class="brand-mark"></span><span class="brand-name">Quorvel<br>Valuations</span></div>

  <div class="photo" style="left:2px;top:97px;width:148px;height:110px;background:linear-gradient(135deg,#3a2a22,#b7723a 45%,#d9c3a4)" role="img" aria-label="Magnifying glass over a small wooden house model"></div>
  <h2 class="abs about-title">ABOUT US</h2>
  <div class="abs about-body">
    <p>We provide property valuation and advisory services to individuals, investors, developers and organisations. Our experts are dedicated to providing high quality valuation advice for every purpose from stamp duty valuations to transactional advice.</p>
    <p>Our emphasis is on providing the most accurate property valuations with transparency, and tailoring our services to meet our clients' individual needs.</p>
    <p>Our reliability and proficiency is underpinned by extensive industry experience, highly qualified valuers, independent outlook and direct and transparent advice which allow us to produce reliable market-leading valuation service across a wide range of property types including residential, commercial, retail and industrial.</p>
    <p>Our professional valuers are all members of the National Property Institute and carry an abundance of experience within the property valuation industry across a broad spectrum of property classes including residential, industrial, commercial and retail sectors.</p>
    <p>Our boutique valuation firm covers the Sydney metropolitan area and beyond including North Sydney and the eastern suburbs, inner city suburbs from Newtown to Strathfield, the greater western Sydney region from Parramatta, Blacktown to Penrith, the Canterbury-Bankstown region and south Sydney region from Hurstville to the Southern Shire.</p>
  </div>

  <h2 class="abs purposes-title">Main purposes for<br>valuation include:</h2>

  <div class="purpose" style="top:119px">
    <svg viewBox="0 0 20 20"><path d="M10 2 1 10h3v8h5v-5h2v5h5v-8h3z"/></svg>
    <div><h3>Pre-Purchase Valuations</h3><p>We provide a completely unbiased valuation service backed by current and relevant sales evidence and market analysis.</p></div>
  </div>
  <div class="purpose" style="top:150px">
    <svg viewBox="0 0 20 20"><text x="10" y="17" text-anchor="middle" font-size="19" font-weight="700" font-family="Roboto,Arial,sans-serif">$</text></svg>
    <div><h3>Stamp Duty Valuations</h3><p>We provide accurate valuations to our clients to ensure they are not paying more stamp duty tax than required.</p></div>
  </div>
  <div class="purpose" style="top:180px">
    <svg viewBox="0 0 20 20"><path d="M2 18h3v-5H2zm4 0h3v-8H6zm4 0h3v-6h-3zm4 0h3V7h-3zM2 10l5-5 4 3 6-6 1 1-7 7-4-3-4 4z"/></svg>
    <div><h3>Capital Gains Tax (CGT)Valuations</h3><p>We are approved to undertake valuations for capital gain tax purposes to the Office of State Revenue; this allows them to calculate the actual amount of tax owed.</p></div>
  </div>
  <div class="purpose" style="top:218px">
    <svg viewBox="0 0 20 20"><path d="M4 1h12v18H4zm2 2v4h8V3zm0 6v2h2V9zm3 0v2h2V9zm3 0v2h2V9zM6 12v2h2v-2zm3 0v2h2v-2zm3 0v5h2v-5zM6 15v2h2v-2zm3 0v2h2v-2z"/></svg>
    <div><h3>Unit Entitlement Valuations</h3><p>We certify that the unit entitlements have been apportioned in an appropriate and legally compliant manner, in accordance with legislation requirements, and based on market value as at the date of valuation</p></div>
  </div>
  <div class="purpose" style="top:260px">
    <svg viewBox="0 0 20 20"><path d="M9 2h2v14h4v2H5v-2h4zM3 5h14v1.5H3zM4 6.5 1 12h6zm12 0L13 12h6zM1 12.5a3 2 0 0 0 6 0zm12 0a3 2 0 0 0 6 0z"/></svg>
    <div><h3>Family Law and Litigation Valuations</h3><p>We handle each case professionally and sensitively, whether acting on behalf of both or either parties. We provide a fair and accurate assessment that can help to assist in this legal process from start to finish.</p></div>
  </div>
  <div class="purpose" style="top:301px">
    <svg viewBox="0 0 20 20"><path d="M9 1h2v2h5v2h-4l3 13h-2l-1-4H8l-1 4H5L8 5H4V3h5zm1 4-1.5 7h3z"/></svg>
    <div><h3>Easement Valuations</h3><p>Quorvel Valuers provide valuations in regards to right to carriageway, right of access, drainage, transmission lines, electrical or sewerage easements.</p></div>
  </div>
  <div class="purpose" style="top:335px">
    <svg viewBox="0 0 20 20"><path d="M4 1h9l4 4v14H4zm2 5v1.5h8V6zm0 3v1.5h8V9zm0 3v1.5h5V12z"/></svg>
    <div><h3>Wills &amp; Probate Valuations</h3><p>Quorvel valuers can provide accurate valuation reports in a timely and sensitive manner to facilitate in the resolution process among the beneficiaries.</p></div>
  </div>
  <div class="purpose" style="top:369px">
    <svg viewBox="0 0 20 20"><circle cx="12" cy="6" r="4"/><path d="M1 12h4l5 2h5l3-2 1 1-4 4H8l-3-1H1z"/></svg>
    <div><h3>Insolvency/Asset Realisation Valuations</h3><p>Our main objective is to facilitate sound assistance and solutions to companies, sole traders and business, which maybe in receivership, bankruptcy, liquidation or voluntary administration. Our personalised valuation reports are to assist in unravelling complex insolvency matters.</p></div>
  </div>

  <h2 class="abs types-tab">The Main Property types</h2>

  <div class="type" style="left:345px;top:93px">
    <div class="photo" role="img" aria-label="Residential apartment buildings with a garden" style="background:linear-gradient(180deg,#a9c9ea,#e4e4df 50%,#6f9650)"></div>
    <h3>Residential Valuations</h3>
    <p>Quorvel valuers provide valuation and advisory to individuals, businesses and financial institutions to assist and add value to all areas of residential investment, being for stamp duty, mortgage, tax or family law related purposes.</p>
    <ul><li>Residential houses</li><li>Vacant land</li><li>Apartments</li><li>Townhouses and villa homes</li><li>Off-the-plan units</li><li>Prestige homes</li><li>Duplex sites</li><li>Heritage-listed properties</li></ul>
  </div>
  <div class="type" style="left:489px;top:92px">
    <div class="photo" role="img" aria-label="Industrial factory interior with machinery" style="background:linear-gradient(180deg,#8e99a6,#d3d6da 50%,#7e858c)"></div>
    <h3>Industrial Valuations</h3>
    <p>Quorvel valuers provide valuation and advisory to individuals, governments, institutions and investors. We assist in all areas of industrial valuations, from small-scale industrial strata units, to large, freestanding industrial buildings.</p>
    <ul><li>Strata titled industrial units</li><li>Freehold industrial buildings</li><li>Workshops</li><li>Vacant industrial development sites</li><li>Self-storage facilities</li></ul>
  </div>
  <div class="type" style="left:347px;top:278px">
    <div class="photo" role="img" aria-label="Glass commercial office tower" style="background:linear-gradient(160deg,#3f6fa8,#1d3457 60%,#5b5a3c)"></div>
    <h3>Commercial Valuations</h3>
    <p>Quorvel valuers provide valuation and advisory to individuals, businesses and financial institutions to assist and add value to all areas of office investment, including those for stamp duty, mortgage, tax, or family-law related purposes.</p>
    <ul><li>Strata titled office suites</li><li>Medical suites</li><li>Freehold commercial buildings</li></ul>
  </div>
  <div class="type" style="left:491px;top:277px">
    <div class="photo" role="img" aria-label="Shopping centre atrium interior" style="background:linear-gradient(180deg,#e8e2d8,#b99f80 60%,#7a6a5a)"></div>
    <h3>Retail Valuations</h3>
    <p>Quorvel valuers provide valuation and advisory to individuals, businesses and financial institutions to assist and add value to all areas of retail investment, being for stamp duty, mortgage, tax or family-law related purposes.</p>
    <ul><li>Strata titled retail suites</li><li>Mixed use retail/residential buildings</li><li>Freehold retail buildings</li></ul>
  </div>
</section>

<!-- Back page -->
<section class="page back">
  <div class="photo" style="left:0;top:0;width:259px;height:235px;background:linear-gradient(180deg,#dfe9f4,#eef0f1 35%,#c9cbcc 70%,#6d8a5a)" role="img" aria-label="White modern apartment building with balconies"></div>
  <svg class="abs turnaround" viewBox="0 0 90 90" aria-hidden="true">
    <path d="M18 22A38 38 0 0 1 80 32" fill="none" stroke="#17703c" stroke-width="2.2"/>
    <path d="M74 30l8 8 3-11z" fill="#17703c"/>
    <path d="M72 68A38 38 0 0 1 10 58" fill="none" stroke="#17703c" stroke-width="2.2"/>
    <path d="M16 60l-8-8-3 11z" fill="#17703c"/>
  </svg>
  <div class="abs turn-num">48</div>
  <div class="abs turn-text">hour turnaround for short form valuations</div>

  <svg class="abs back-green" viewBox="0 0 259 120" preserveAspectRatio="none" aria-hidden="true">
    <path d="M0 12Q130 6 259 0V120H0z" fill="#5ea57a"/>
    <path d="M0 22Q130 16 259 16V108Q130 112 0 106z" fill="#17703c"/>
    <path d="M0 106Q130 112 259 108V120H0z" fill="#0f5e31"/>
  </svg>
  <svg class="abs" style="left:7px;top:242px;width:16px;height:22px" viewBox="0 0 16 22" aria-hidden="true">
    <circle cx="8" cy="8" r="6.5" fill="none" stroke="#fff" stroke-width="1.4"/>
    <path d="M5 8l2 2 4-4" fill="none" stroke="#fff" stroke-width="1.4"/>
    <path d="M4 13l-2 8 3-2 2 2 1-6M12 13l2 8-3-2-2 2-1-6" fill="#fff"/>
  </svg>
  <h2 class="abs guarantee-title">Our Guarantee:</h2>
  <ul class="abs guarantee-list">
    <li>One on one interaction</li>
    <li>Free quote and initial consultation</li>
    <li>Reliable service turnaround time</li>
    <li>Value adding to our clients' long-term goals</li>
    <li>Highly qualified valuers</li>
    <li>Building successful and sustained working relationships</li>
  </ul>
  <div class="abs divider"></div>
  <h2 class="abs contact-title">Reach out to us today</h2>
  <ul class="abs contact-list">
    <li><svg viewBox="0 0 10 10"><path d="M2 0h2l1 3-1.5 1a6 6 0 0 0 2.5 2.5L7 5l3 1v2c0 1-1 2-2 2A8 8 0 0 1 0 2c0-1 1-2 2-2z"/></svg>1300 000 555</li>
    <li><svg viewBox="0 0 10 10"><path d="M0 2h10v6H0zm1 .8v.4L5 6l4-2.8v-.4L5 5.4z"/></svg>info@quorvelvaluations-example.com.au</li>
    <li><svg viewBox="0 0 10 10"><path d="M0 2h10v6H0zm1 1v1h3V3zm0 2v1h3V5zm5-2v3h3V3z"/></svg>PO Box 100 Exampleton NSW 2000</li>
    <li><svg viewBox="0 0 10 10"><path d="M5 0a5 5 0 1 0 0 10A5 5 0 0 0 5 0zm0 1c.8.8 1.3 2 1.4 3.5H3.6C3.7 3 4.2 1.8 5 1zM1 5.5h1.6C2.7 6.8 3 8 3.6 8.7A4 4 0 0 1 1 5.5zm2.6 0h2.8C6.3 7 5.8 8.2 5 9c-.8-.8-1.3-2-1.4-3.5zm3.8 0H9a4 4 0 0 1-2.6 3.2c.6-.7.9-1.9 1-3.2zM1 4.5A4 4 0 0 1 3.6 1.3C3 2 2.7 3.2 2.6 4.5zm6.4 0C7.3 3.2 7 2 6.4 1.3A4 4 0 0 1 9 4.5z"/></svg>www.quorvelvaluations-example.com.au</li>
  </ul>
  <div class="brand"><span class="brand-mark"></span><span class="brand-name">Quorvel<br>Valuations</span></div>
  <div class="badge" style="left:195px;top:339px;width:46px;height:19px"></div>
</section>

</body>
</html>
```